Frostwyn.co - Polar Expeditions Specialists

We need a modern, visually striking business card for Frostwyn.co, a company specialized in selling expedition cruises to the most remote regions on Earth, with a focus on the Arctic and Antarctica. The design should instantly communicate that the cardholder is an expert in polar travel. Use clean, premium aesthetics with cool tones like icy blue and white, possibly incorporating polar imagery (ice, glaciers, penguins, etc.)

Attached the logo

Contact Information for Business Card

Feels high-end and trustworthy.. Visually memorable — encourages people to keep it

Colors
0054AA
0677BA
7BADD7
CADEEF
E8F1F8

Requirements
Must have
• ice, glaciers, penguins, montains
Nice to have
• modern, transparente,

```html
<!DOCTYPE html>
<html lang="en">
<head>
<meta charset="UTF-8">
<title>Frostwyn.co – Business Card</title>
<link href="https://fonts.googleapis.com/css2?family=Poppins:wght@300;400;600;700&display=swap" rel="stylesheet">
<style>
  :root {
    --bg: #e8f1f8;
    --ink: #23253a;
    --white: #ffffff;
    --sky-top: #f4f6f8;
    --sky-mid: #d9e1e7;
    --ice: #c9d8e2;
    --water: #5f7480;
    --water-deep: #3d4f59;
    --back-sky: #9fb6c8;
    --back-sky-light: #c4d4e0;
  }
  * { margin: 0; padding: 0; box-sizing: border-box; }
  html, body { width: 1200px; height: 913px; overflow: hidden; }
  body {
    background: var(--bg);
    font-family: "Poppins", sans-serif;
    position: relative;
  }
  .card {
    position: absolute;
    width: 600px;
    height: 343px;
    border-radius: 28px;
    overflow: hidden;
    box-shadow: 0 14px 34px rgba(35, 37, 58, 0.22);
  }
  .card--front { left: 70px; top: 70px; }
  .card--back { left: 530px; top: 500px; }
  .card__photo { position: absolute; inset: 0; }
  .card--front .card__photo {
    background: linear-gradient(180deg, var(--sky-top) 0%, var(--sky-mid) 42%, var(--ice) 58%, var(--water) 78%, var(--water-deep) 100%);
  }
  .card--back .card__photo {
    background: linear-gradient(180deg, var(--back-sky-light) 0%, var(--back-sky) 40%, var(--ice) 56%, var(--water) 76%, var(--water-deep) 100%);
  }
  .brand { position: absolute; color: var(--ink); }
  .brand__name {
    display: flex; align-items: center; gap: 10px;
    font-weight: 700; font-size: 44px; line-height: 1; letter-spacing: -0.5px;
  }
  .brand__dot { width: 14px; height: 14px; border-radius: 50%; background: var(--ink); }
  .brand__tagline { font-weight: 600; font-size: 11.5px; margin-top: 6px; padding-left: 24px; }
  .card--front .brand { right: 40px; top: 52px; }
  .card--back .brand { left: 150px; top: 60px; }
  .front__web {
    position: absolute; right: 42px; bottom: 118px;
    font-weight: 700; font-size: 15px; letter-spacing: 7px; color: var(--ink);
  }
  .holder { position: absolute; left: 200px; top: 150px; color: var(--ink); }
  .holder__name { font-weight: 700; font-size: 18px; letter-spacing: 0.5px; }
  .holder__role { font-weight: 300; font-size: 16px; }
  .contact {
    position: absolute; left: 30px; bottom: 26px;
    color: var(--white); font-size: 17px; font-weight: 400;
    list-style: none;
  }
  .contact li { display: flex; align-items: center; gap: 10px; line-height: 1.55; }
  .contact svg { width: 16px; height: 16px; flex: none; }
  .address {
    position: absolute; right: 34px; bottom: 150px;
    color: var(--white); font-size: 17px; font-weight: 400; text-align: right; line-height: 1.3;
  }
</style>
</head>
<body>

<section class="card card--front">
  <div class="card__photo" role="img" aria-label="Photograph of penguins standing on a floating iceberg under a pale sky above grey sea"></div>
  <div class="brand">
    <div class="brand__name"><span class="brand__dot"></span>Frostwyn.co</div>
    <div class="brand__tagline">Polar Expeditions Specialists</div>
  </div>
  <div class="front__web">www.frostwyn.co</div>
</section>

<section class="card card--back">
  <div class="card__photo" role="img" aria-label="Photograph of penguins on an iceberg edge with icy sea below"></div>
  <div class="brand">
    <div class="brand__name"><span class="brand__dot"></span>Frostwyn.co</div>
    <div class="brand__tagline">Polar Expeditions Specialists</div>
  </div>
  <div class="holder">
    <div class="holder__name">ERIK HALVORSEN</div>
    <div class="holder__role">Expeditions Specialists</div>
  </div>
  <div class="address">00 dummy city<br>dummy place 0000</div>
  <ul class="contact">
    <li>
      <svg viewBox="0 0 24 24" fill="var(--white)"><path d="M6.6 10.8a15.1 15.1 0 0 0 6.6 6.6l2.2-2.2a1 1 0 0 1 1-.25 11.4 11.4 0 0 0 3.6.57 1 1 0 0 1 1 1V20a1 1 0 0 1-1 1A17 17 0 0 1 3 4a1 1 0 0 1 1-1h3.5a1 1 0 0 1 1 1c0 1.25.2 2.45.57 3.57a1 1 0 0 1-.25 1z"/></svg>
      300-555-0142
    </li>
    <li>
      <svg viewBox="0 0 24 24" fill="none" stroke="var(--white)" stroke-width="2"><rect x="3" y="5" width="18" height="14" rx="1"/><path d="M3 6l9 7 9-7"/></svg>
      erik@frostwyn.co
    </li>
    <li>
      <svg viewBox="0 0 24 24" fill="none" stroke="var(--white)" stroke-width="1.6"><circle cx="12" cy="12" r="9"/><path d="M3 12h18M12 3c3 3 3 15 0 18M12 3c-3 3-3 15 0 18"/></svg>
      www.frostwyn.co
    </li>
  </ul>
</section>

</body>
</html>
```